Honey Labels for Manuka, Rewarewa, Multifloral and Manuka Blend honey

We require 4 label designs for our 4 types of honey i.e. Manuka, Rewarewa, Multifloral and Manuka Blend. Each design should be adapted for 250g, 500g, and 1kg PET jars. The design should look friendly and professional.

Tare: amber Square mason PET jars (see images attached)
Jar dimensions: see PDF attached

Target Market(s)

Worldwide. People caring for their health.

Industry/Entity Type

Health Product

Font styles to use
Serif
Decorative

Colors
6a429a
f37122
0692cd
9bcb3c

Requirements
Must have
• Each label should contain the following information
• • name of the honey e.g. Manuka Honey
• • VelnorTM logo (provided)
• • an image of a bird (provided),
• • nutrition table
• • a bar code
• • a place for a batch number and the best before date to be printed
• • volume: e.g. 250g, 500g, 1kg
• • Text: “Product of New Zealand”
• • Text: “Produced & packed by: Dostrel’s Combs Ltd. 87B Kelvanie Road, Tauranga 3148, New Zealand sales@velnorhoney.co.nz www.velnorhoney.co.nz
• • Ingredients: 100% Pure Raw New Zealand Honey
• • Text: “All specified values are averages.”
• • Not suitable for infants under 12 months. Do not use if cap seal is broken. Production methods involved with this product are not-GM. Contains bee products.
• • PET Recycling pictogram
• • Round corners
• Apart from different bird image each of 4 honey labels should have it's own color element e.g a different color background or a line.
• The birds:
• • Manuka honey: image of a Kingfisher bird
• o MGO Pictogram (80+, 100+, 200+, 300+ or 400+)
• • Rewarewa honey: image of a Kereru bird
• • Multifloral honey: image of a Tui bird
• • Manuka blend: image of a Pukekohe bird
Should not have
• Disclaimer: The provided images of birds is a copyright content. It is prohibited to use them outside of this project.

```html
<!DOCTYPE html>
<html lang="en">
<head>
<meta charset="utf-8">
<title>Velnor Honey Labels</title>
<link rel="stylesheet" href="https://fonts.googleapis.com/css2?family=Arimo:ital,wght@0,400;0,700;1,400&family=Cinzel:wght@400&family=Tinos&display=swap">
<style>
  :root {
    --stage: #808080;
    --paper: #ffffff;
    --ink: #ffffff;
    --logo: #c9a55c;
    --rewarewa: #6a429a;
    --rewarewa-light: #7650a7;
    --blend: #1b95d2;
    --blend-light: #2ba3de;
    --multi: #9bcb3c;
    --multi-light: #b4d433;
    --manuka: #f37122;
    --manuka-light: #f5862b;
  }
  * { box-sizing: border-box; margin: 0; padding: 0; }
  html, body { width: 1101px; height: 1200px; overflow: hidden; }
  body {
    background: var(--stage);
    position: relative;
    font-family: "Arimo", Arial, sans-serif;
    color: var(--ink);
  }
  .label {
    position: absolute;
    left: 18px;
    width: 1066px;
    height: 248px;
    background: var(--paper);
    border-radius: 10px;
  }
  .label--rewarewa { top: 50px;  --c: var(--rewarewa); --c-light: var(--rewarewa-light); }
  .label--blend    { top: 345px; --c: var(--blend);    --c-light: var(--blend-light); }
  .label--multi    { top: 642px; --c: var(--multi);    --c-light: var(--multi-light); }
  .label--manuka   { top: 940px; --c: var(--manuka);   --c-light: var(--manuka-light); }

  .tab {
    position: absolute;
    left: 454px;
    top: -44px;
    width: 152px;
    height: 64px;
  }
  .tab svg { position: absolute; inset: 0; }
  .tab path { fill: var(--c); }
  .brand {
    position: absolute;
    left: 0; right: 0; top: 14px;
    text-align: center;
    font-family: "Cinzel", "Times New Roman", serif;
    font-size: 13px;
    letter-spacing: 1px;
    color: var(--logo);
  }
  .brand-dot {
    display: block;
    width: 7px; height: 7px;
    margin: 0 auto 3px;
    border-radius: 50%;
    background: var(--logo);
  }

  .band {
    position: absolute;
    left: 9px; top: 18px;
    width: 1050px; height: 208px;
    border-radius: 6px;
    background: linear-gradient(to bottom,
      var(--c) 0, var(--c) 44px,
      var(--c-light) 44px, var(--c-light) 134px,
      var(--c) 134px);
  }

  .assurance {
    position: absolute;
    left: 16px; top: 13px;
    width: 310px;
    font-size: 8.2px;
    line-height: 10px;
  }
  .assurance p { margin-bottom: 10px; }
  .assurance p:nth-child(2) { margin-top: 8px; }

  .packer {
    position: absolute;
    left: 152px; top: 125px;
    font-size: 8.2px;
    line-height: 10px;
  }
  .packer strong { font-weight: 700; }
  .packer .web { margin-top: 10px; font-style: italic; }

  .bird {
    position: absolute;
    z-index: 1;
    opacity: .9;
  }
  .label--rewarewa .bird { left: 606px; top: -8px;  width: 100px; height: 222px; border-radius: 45% 45% 30% 30%; background: linear-gradient(160deg, #4fc9a0, #3b7fa8 45%, #e9e4ee 75%, #b04f8e); }
  .label--blend .bird    { left: 606px; top: -14px; width: 106px; height: 232px; border-radius: 45% 45% 30% 30%; background: linear-gradient(170deg, #d93447, #4f3e9c 25%, #2d3790 60%, #f07b96); }
  .label--multi .bird    { left: 548px; top: 19px;  width: 160px; height: 196px; border-radius: 40%; background: linear-gradient(150deg, #2b8ab0, #1a5d83 45%, #f2b81e 60%, #6b5a49); }
  .label--manuka .bird   { left: 545px; top: 14px;  width: 168px; height: 160px; border-radius: 45%; background: linear-gradient(150deg, #2a3a8c, #2ea6e6 40%, #74d3f2 65%, #5a6fb0); }

  .product {
    position: absolute;
    left: 366px; top: 52px;
    z-index: 2;
  }
  .product .pure {
    font-family: "Tinos", "Times New Roman", serif;
    font-size: 11.5px;
  }
  .product h2 {
    margin-top: 6px;
    font-family: "Cinzel", "Times New Roman", serif;
    font-weight: 400;
    font-size: 25px;
    line-height: 30px;
    letter-spacing: .5px;
  }
  .weight {
    position: absolute;
    left: 483px; top: 142px;
    width: 80px;
    text-align: center;
    font-size: 13.5px;
    line-height: 14px;
    z-index: 2;
  }
  .origin {
    position: absolute;
    left: 423px; top: 185px;
    width: 200px;
    display: flex; align-items: center; justify-content: center; gap: 6px;
    font-size: 12px;
    z-index: 2;
  }
  .origin-mark {
    width: 16px; height: 14px;
    border-radius: 50%;
    background: rgba(0,0,0,.18);
  }

  .nutrition {
    position: absolute;
    left: 721px; top: 18px;
    width: 168px; height: 144px;
    border: 1px solid var(--ink);
    border-radius: 6px;
    padding: 5px 8px;
    font-size: 8px;
    line-height: 10px;
    z-index: 2;
  }
  .nutrition .head { font-weight: 700; }
  .nutrition .head span { font-weight: 400; }
  .nutrition hr { border: 0; border-top: 1px solid var(--ink); margin: 3px -8px; }
  .nutrition table { width: 100%; border-collapse: collapse; }
  .nutrition th { font-weight: 400; text-align: center; padding-bottom: 8px; }
  .nutrition td { padding: 0; }
  .nutrition td + td { text-align: center; }
  .averages {
    position: absolute;
    left: 721px; top: 167px;
    width: 168px;
    text-align: center;
    font-size: 8.2px;
    z-index: 2;
  }

  .notes {
    position: absolute;
    left: 901px; top: 18px;
    width: 142px;
    font-size: 8.2px;
    line-height: 10px;
  }
  .notes p { margin-bottom: 10px; }
  .notes strong { font-weight: 700; }

  .recycle {
    position: absolute;
    left: 995px; top: 144px;
    width: 42px; height: 42px;
  }
</style>
</head>
<body>

<section class="label label--rewarewa">
  <div class="tab">
    <svg viewBox="0 0 152 64" width="152" height="64"><path d="M0 64 Q12 64 12 50 L12 24 Q12 5 40 3 Q76 -1 112 3 Q140 5 140 24 L140 50 Q140 64 152 64 Z"/></svg>
    <div class="brand"><span class="brand-dot"></span>VELNOR</div>
  </div>
  <div class="band">
    <div class="assurance">
      <p>Buying our Manuka honey, you can be 100% sure you buy the genuine Manuka honey as all of our honeys are tested by independent scientific laboratory for methylglyoxal (MGO) and dihydroxyacetone concentration.</p>
      <p>Here at Dostrel’s Combs we operate under Risk Management Program (RMP) which is based on Hazard Analysis &amp; Critical Control Points (HACCP) food safety principles and a NZFSA Approved Premises for Processing Bee Products.</p>
      <p>Dostrel’s Combs is a registered exporter of Animal Products under New Zealand Food Safety Authority (NZFSA).</p>
    </div>
    <div class="packer">
      <strong>Produced &amp; Packed by:</strong><br>Dostrel’s Combs Ltd<br>87B Kelvanie Road, Tauranga 3148<br>New Zealand
      <div class="web">sales@velnorhoney.co.nz<br>www.velnorhoney.co.nz</div>
    </div>
    <div class="bird" role="img" aria-label="Geometric illustration of a kereru pigeon"></div>
    <div class="product"><div class="pure">100% Pure NZ</div><h2>REWAREWA<br>HONEY</h2></div>
    <div class="weight">250g<br>Net</div>
    <div class="origin">Product of <span class="origin-mark" role="img" aria-label="Small kiwi bird icon"></span> New Zealand</div>
    <div class="nutrition">
      <div class="head">Nutritional Information<br>Servings per package: <span>50</span><br>Serving size: <span>10g</span></div>
      <hr>
      <table>
        <tr><th></th><th>Average<br>per serving</th><th>Average<br>per 100g</th></tr>
        <tr><td>Energy</td><td>132 kJ</td><td>1320 kJ</td></tr>
        <tr><td>Protein</td><td>Less than 1g</td><td>0.4g</td></tr>
        <tr><td>Fat Total</td><td>0 g</td><td>0 g</td></tr>
        <tr><td>&nbsp;-saturated</td><td>0 g</td><td>0 g</td></tr>
        <tr><td>Carbohydrates</td><td>8 g</td><td>80 g</td></tr>
        <tr><td>&nbsp;-sugars</td><td>7.8 g</td><td>78 g</td></tr>
        <tr><td>Sodium</td><td>1.2 mg</td><td>12 mg</td></tr>
      </table>
    </div>
    <div class="averages">All specified values are averages</div>
    <div class="notes">
      <p><strong>Ingredients:</strong> 100% Pure Raw New Zealand Honey</p>
      <p>Not suitable for infants under 12 months.<br>Do not use if cap seal is broken.<br>Production methods involved with this product are not-GM.<br>Contains bee products<br>Store below 20°C</p>
    </div>
    <svg class="recycle" viewBox="0 0 42 42" role="img" aria-label="Recycling symbol"><g fill="none" stroke="#fff" stroke-width="5" stroke-linejoin="round"><path d="M15 12 L21 3 L27 12"/><path d="M32 17 L38 28 L29 36"/><path d="M14 37 L4 29 L10 18"/></g><g fill="#fff"><path d="M26 6 L34 8 L28 15 Z"/><path d="M35 36 L26 39 L27 30 Z"/><path d="M4 19 L12 14 L14 23 Z"/></g></svg>
  </div>
</section>

<section class="label label--blend">
  <div class="tab">
    <svg viewBox="0 0 152 64" width="152" height="64"><path d="M0 64 Q12 64 12 50 L12 24 Q12 5 40 3 Q76 -1 112 3 Q140 5 140 24 L140 50 Q140 64 152 64 Z"/></svg>
    <div class="brand"><span class="brand-dot"></span>VELNOR</div>
  </div>
  <div class="band">
    <div class="assurance">
      <p>Buying our Manuka honey, you can be 100% sure you buy the genuine Manuka honey as all of our honeys are tested by independent scientific laboratory for methylglyoxal (MGO) and dihydroxyacetone concentration.</p>
      <p>Here at Dostrel’s Combs we operate under Risk Management Program (RMP) which is based on Hazard Analysis &amp; Critical Control Points (HACCP) food safety principles and a NZFSA Approved Premises for Processing Bee Products.</p>
      <p>Dostrel’s Combs is a registered exporter of Animal Products under New Zealand Food Safety Authority (NZFSA).</p>
    </div>
    <div class="packer">
      <strong>Produced &amp; Packed by:</strong><br>Dostrel’s Combs Ltd<br>87B Kelvanie Road, Tauranga 3148<br>New Zealand
      <div class="web">sales@velnorhoney.co.nz<br>www.velnorhoney.co.nz</div>
    </div>
    <div class="bird" role="img" aria-label="Geometric illustration of a pukeko swamphen"></div>
    <div class="product"><div class="pure">100% Pure NZ</div><h2>MANUKA<br>BLEND</h2></div>
    <div class="weight">250g<br>Net</div>
    <div class="origin">Product of <span class="origin-mark" role="img" aria-label="Small kiwi bird icon"></span> New Zealand</div>
    <div class="nutrition">
      <div class="head">Nutritional Information<br>Servings per package: <span>50</span><br>Serving size: <span>10g</span></div>
      <hr>
      <table>
        <tr><th></th><th>Average<br>per serving</th><th>Average<br>per 100g</th></tr>
        <tr><td>Energy</td><td>132 kJ</td><td>1320 kJ</td></tr>
        <tr><td>Protein</td><td>Less than 1g</td><td>0.4g</td></tr>
        <tr><td>Fat Total</td><td>0 g</td><td>0 g</td></tr>
        <tr><td>&nbsp;-saturated</td><td>0 g</td><td>0 g</td></tr>
        <tr><td>Carbohydrates</td><td>8 g</td><td>80 g</td></tr>
        <tr><td>&nbsp;-sugars</td><td>7.8 g</td><td>78 g</td></tr>
        <tr><td>Sodium</td><td>1.2 mg</td><td>12 mg</td></tr>
      </table>
    </div>
    <div class="averages">All specified values are averages</div>
    <div class="notes">
      <p><strong>Ingredients:</strong> 100% Pure Raw New Zealand Honey</p>
      <p>Not suitable for infants under 12 months.<br>Do not use if cap seal is broken.<br>Production methods involved with this product are not-GM.<br>Contains bee products<br>Store below 20°C</p>
    </div>
    <svg class="recycle" viewBox="0 0 42 42" role="img" aria-label="Recycling symbol"><g fill="none" stroke="#fff" stroke-width="5" stroke-linejoin="round"><path d="M15 12 L21 3 L27 12"/><path d="M32 17 L38 28 L29 36"/><path d="M14 37 L4 29 L10 18"/></g><g fill="#fff"><path d="M26 6 L34 8 L28 15 Z"/><path d="M35 36 L26 39 L27 30 Z"/><path d="M4 19 L12 14 L14 23 Z"/></g></svg>
  </div>
</section>

<section class="label label--multi">
  <div class="tab">
    <svg viewBox="0 0 152 64" width="152" height="64"><path d="M0 64 Q12 64 12 50 L12 24 Q12 5 40 3 Q76 -1 112 3 Q140 5 140 24 L140 50 Q140 64 152 64 Z"/></svg>
    <div class="brand"><span class="brand-dot"></span>VELNOR</div>
  </div>
  <div class="band">
    <div class="assurance">
      <p>Buying our Manuka honey, you can be 100% sure you buy the genuine Manuka honey as all of our honeys are tested by independent scientific laboratory for methylglyoxal (MGO) and dihydroxyacetone concentration.</p>
      <p>Here at Dostrel’s Combs we operate under Risk Management Program (RMP) which is based on Hazard Analysis &amp; Critical Control Points (HACCP) food safety principles and a NZFSA Approved Premises for Processing Bee Products.</p>
      <p>Dostrel’s Combs is a registered exporter of Animal Products under New Zealand Food Safety Authority (NZFSA).</p>
    </div>
    <div class="packer">
      <strong>Produced &amp; Packed by:</strong><br>Dostrel’s Combs Ltd<br>87B Kelvanie Road, Tauranga 3148<br>New Zealand
      <div class="web">sales@velnorhoney.co.nz<br>www.velnorhoney.co.nz</div>
    </div>
    <div class="bird" role="img" aria-label="Geometric illustration of a tui perched on a flowering branch"></div>
    <div class="product"><div class="pure">100% Pure NZ</div><h2>MULTIFLORAL<br>HONEY</h2></div>
    <div class="weight">250g<br>Net</div>
    <div class="origin">Product of <span class="origin-mark" role="img" aria-label="Small kiwi bird icon"></span> New Zealand</div>
    <div class="nutrition">
      <div class="head">Nutritional Information<br>Servings per package: <span>50</span><br>Serving size: <span>10g</span></div>
      <hr>
      <table>
        <tr><th></th><th>Average<br>per serving</th><th>Average<br>per 100g</th></tr>
        <tr><td>Energy</td><td>132 kJ</td><td>1320 kJ</td></tr>
        <tr><td>Protein</td><td>Less than 1g</td><td>0.4g</td></tr>
        <tr><td>Fat Total</td><td>0 g</td><td>0 g</td></tr>
        <tr><td>&nbsp;-saturated</td><td>0 g</td><td>0 g</td></tr>
        <tr><td>Carbohydrates</td><td>8 g</td><td>80 g</td></tr>
        <tr><td>&nbsp;-sugars</td><td>7.8 g</td><td>78 g</td></tr>
        <tr><td>Sodium</td><td>1.2 mg</td><td>12 mg</td></tr>
      </table>
    </div>
    <div class="averages">All specified values are averages</div>
    <div class="notes">
      <p><strong>Ingredients:</strong> 100% Pure Raw New Zealand Honey</p>
      <p>Not suitable for infants under 12 months.<br>Do not use if cap seal is broken.<br>Production methods involved with this product are not-GM.<br>Contains bee products<br>Store below 20°C</p>
    </div>
    <svg class="recycle" viewBox="0 0 42 42" role="img" aria-label="Recycling symbol"><g fill="none" stroke="#fff" stroke-width="5" stroke-linejoin="round"><path d="M15 12 L21 3 L27 12"/><path d="M32 17 L38 28 L29 36"/><path d="M14 37 L4 29 L10 18"/></g><g fill="#fff"><path d="M26 6 L34 8 L28 15 Z"/><path d="M35 36 L26 39 L27 30 Z"/><path d="M4 19 L12 14 L14 23 Z"/></g></svg>
  </div>
</section>

<section class="label label--manuka">
  <div class="tab">
    <svg viewBox="0 0 152 64" width="152" height="64"><path d="M0 64 Q12 64 12 50 L12 24 Q12 5 40 3 Q76 -1 112 3 Q140 5 140 24 L140 50 Q140 64 152 64 Z"/></svg>
    <div class="brand"><span class="brand-dot"></span>VELNOR</div>
  </div>
  <div class="band">
    <div class="assurance">
      <p>Buying our Manuka honey, you can be 100% sure you buy the genuine Manuka honey as all of our honeys are tested by independent scientific laboratory for methylglyoxal (MGO) and dihydroxyacetone concentration.</p>
      <p>Here at Dostrel’s Combs we operate under Risk Management Program (RMP) which is based on Hazard Analysis &amp; Critical Control Points (HACCP) food safety principles and a NZFSA Approved Premises for Processing Bee Products.</p>
      <p>Dostrel’s Combs is a registered exporter of Animal Products under New Zealand Food Safety Authority (NZFSA).</p>
    </div>
    <div class="packer">
      <strong>Produced &amp; Packed by:</strong><br>Dostrel’s Combs Ltd<br>87B Kelvanie Road, Tauranga 3148<br>New Zealand
      <div class="web">sales@velnorhoney.co.nz<br>www.velnorhoney.co.nz</div>
    </div>
    <div class="bird" role="img" aria-label="Geometric illustration of a kingfisher on a branch"></div>
    <div class="product"><div class="pure">100% Pure NZ</div><h2>MANUKA<br>HONEY</h2></div>
    <div class="weight">250g<br>Net</div>
    <div class="origin">Product of <span class="origin-mark" role="img" aria-label="Small kiwi bird icon"></span> New Zealand</div>
    <div class="nutrition">
      <div class="head">Nutritional Information<br>Servings per package: <span>50</span><br>Serving size: <span>10g</span></div>
      <hr>
      <table>
        <tr><th></th><th>Average<br>per serving</th><th>Average<br>per 100g</th></tr>
        <tr><td>Energy</td><td>132 kJ</td><td>1320 kJ</td></tr>
        <tr><td>Protein</td><td>Less than 1g</td><td>0.4g</td></tr>
        <tr><td>Fat Total</td><td>0 g</td><td>0 g</td></tr>
        <tr><td>&nbsp;-saturated</td><td>0 g</td><td>0 g</td></tr>
        <tr><td>Carbohydrates</td><td>8 g</td><td>80 g</td></tr>
        <tr><td>&nbsp;-sugars</td><td>7.8 g</td><td>78 g</td></tr>
        <tr><td>Sodium</td><td>1.2 mg</td><td>12 mg</td></tr>
      </table>
    </div>
    <div class="averages">All specified values are averages</div>
    <div class="notes">
      <p><strong>Ingredients:</strong> 100% Pure Raw New Zealand Honey</p>
      <p>Not suitable for infants under 12 months.<br>Do not use if cap seal is broken.<br>Production methods involved with this product are not-GM.<br>Contains bee products<br>Store below 20°C</p>
    </div>
    <svg class="recycle" viewBox="0 0 42 42" role="img" aria-label="Recycling symbol"><g fill="none" stroke="#fff" stroke-width="5" stroke-linejoin="round"><path d="M15 12 L21 3 L27 12"/><path d="M32 17 L38 28 L29 36"/><path d="M14 37 L4 29 L10 18"/></g><g fill="#fff"><path d="M26 6 L34 8 L28 15 Z"/><path d="M35 36 L26 39 L27 30 Z"/><path d="M4 19 L12 14 L14 23 Z"/></g></svg>
  </div>
</section>

</body>
</html>
```